UK Supplement Company Needs a Label for Diet Protein Powder

We need a new, modern and fresh design for our Diet Protein Powder. Our protein powder is packaged in black plastic tubs (photo attached) and needs an attractive label. We would like to see designs that grab attention and look professional. We're very open to ideas. The label should be 88mm x 365mm. We also prefer PSD format where possible. These alterations could be made once your design is chosen. Have attached photo of our shake ingredients/benefits.
Updates

Need extra days to review

Target Market(s)

Slimmers

Industry/Entity Type

Health And Wellness

Font styles to use
Serif
Sans Serif

Colors

Designer to choose colors to be used in the design.

Requirements
Must have
• Clean, Modern and Professional Look. Eye catching. The flavour, we offer 6 flavours so this must be something we can edit (Flavours are Banana, Chocolate, Chocolate Mint, Strawberry, Toffee and Vanilla).
Nice to have
• Our logo, this can be VELTRA Nutrition or just VELTRA. Our logo files are attached.
Should not have
• We do not want to see people (faces or bodies) on the design.

```html
<!DOCTYPE html>
<html lang="en">
<head>
<meta charset="UTF-8">
<title>VELTRA Nutrition – Diet Protein Power Labels</title>
<link href="https://fonts.googleapis.com/css2?family=Roboto:wght@400;500;700;900&family=Roboto+Condensed:wght@700&display=swap" rel="stylesheet">
<style>
  :root {
    --bg: #ffffff;
    --label: #e9eaeb;
    --ink: #111111;
    --dark: #141414;
    --brand-text: #ffffff;
    --brand-sub: #cfcfcf;
    --stat-label: #dddddd;
    --accent-green: #9cc43a;
    --stat-orange: #f0a64a;
    --stat-red: #e8584e;
    --stat-yellow: #f3c21c;
    --choc: #8a4e26;
    --straw: #d9464a;
    --banana: #e3bd2a;
  }
  * { margin: 0; padding: 0; box-sizing: border-box; }
  html, body { width: 1200px; height: 960px; overflow: hidden; background: var(--bg); }
  body { font-family: "Roboto", Arial, sans-serif; color: var(--ink); }

  .range {
    position: absolute; top: 320px; left: 30px;
    display: flex; gap: 30px;
  }
  .label {
    position: relative; width: 360px; height: 320px;
    background: var(--label); overflow: hidden;
  }
  .label--chocolate { --flavour: var(--choc); }
  .label--strawberry { --flavour: var(--straw); }
  .label--banana { --flavour: var(--banana); }

  .swoosh { position: absolute; inset: 0; width: 360px; height: 320px; }
  .swoosh .band { fill: var(--flavour); }
  .swoosh .edge { fill: none; stroke: var(--ink); stroke-width: 3; }
  .swoosh .strip { fill: var(--dark); }

  .brand {
    position: absolute; left: 8px; top: 22px; width: 26px; height: 130px;
  }
  .brand-name {
    writing-mode: vertical-rl; font-weight: 900; font-size: 22px;
    color: var(--brand-text); letter-spacing: 1px; line-height: 1;
  }
  .brand-sub {
    position: absolute; left: 31px; top: 24px;
    writing-mode: vertical-rl; font-size: 6px; letter-spacing: 3px; color: var(--brand-sub);
  }

  .title {
    position: absolute; right: 52px; top: 44px; text-align: right; line-height: 0.95;
  }
  .title-diet { font-size: 44px; font-weight: 700; }
  .title-protein { font-size: 52px; font-weight: 900; letter-spacing: -1px; }
  .title-power { font-size: 30px; font-weight: 500; margin-top: 4px; }
  .rule {
    position: absolute; right: 52px; top: 226px; width: 128px; height: 2px;
    background: var(--accent-green);
  }
  .claims {
    position: absolute; right: 52px; top: 236px; text-align: right;
    font-size: 14px; font-weight: 500; line-height: 1.4;
  }

  .flavour-art {
    position: absolute; left: 60px; top: 192px; width: 120px; height: 70px;
    border-radius: 10px;
    background: radial-gradient(ellipse at center, var(--flavour), rgba(0,0,0,0) 72%);
  }

  .flavour-tag {
    position: absolute; left: 46px; top: 290px; width: 140px; height: 24px;
    background: var(--flavour); color: var(--ink);
    font-size: 13px; font-weight: 500; letter-spacing: 1.5px;
    display: flex; align-items: center; justify-content: center;
  }
  .net-weight {
    position: absolute; right: 52px; top: 297px; font-size: 10px; font-weight: 500;
  }

  .stats {
    position: absolute; right: 8px; top: 14px; width: 36px; height: 210px;
    background: var(--dark); border-radius: 4px;
    display: flex; flex-direction: column; align-items: center; justify-content: space-around;
    padding: 6px 0; text-align: center;
  }
  .stat-value {
    font-family: "Roboto Condensed", "Arial Narrow", sans-serif; font-weight: 700;
    font-size: 11px; line-height: 1; white-space: nowrap;
  }
  .stat-value--cal { color: var(--stat-orange); }
  .stat-value--protein { color: var(--stat-red); }
  .stat-value--carbs { color: var(--stat-yellow); }
  .stat-value--vit { color: var(--stat-orange); }
  .stat-name { font-size: 4.5px; color: var(--stat-label); text-transform: uppercase; line-height: 1.2; margin-top: 2px; }
</style>
</head>
<body>
<main class="range">

  <section class="label label--chocolate">
    <svg class="swoosh" viewBox="0 0 360 320" aria-hidden="true">
      <rect class="strip" x="0" y="0" width="40" height="320"/>
      <path class="band" d="M40 0 H140 C112 60 100 110 84 180 C70 240 60 290 56 320 H40 Z"/>
      <path class="edge" d="M140 0 C112 60 100 110 84 180 C70 240 60 290 56 320"/>
    </svg>
    <div class="brand"><span class="brand-name">VELTRA</span></div>
    <span class="brand-sub">NUTRITION</span>
    <div class="title">
      <div class="title-diet">DIET</div>
      <div class="title-protein">PROTEIN</div>
      <div class="title-power">POWER</div>
    </div>
    <div class="flavour-art" role="img" aria-label="Photo of chocolate bar pieces"></div>
    <div class="rule"></div>
    <p class="claims">High Protein<br>Low Carbohydrates</p>
    <div class="flavour-tag">CHOCOLATE</div>
    <p class="net-weight">NET WT. 6lb (2.727G)</p>
    <div class="stats">
      <div><div class="stat-value stat-value--cal">1050</div><div class="stat-name">Calories</div></div>
      <div><div class="stat-value stat-value--protein">60G</div><div class="stat-name">Protein</div></div>
      <div><div class="stat-value stat-value--carbs">250G+</div><div class="stat-name">Carbs</div></div>
      <div><div class="stat-value stat-value--vit">30</div><div class="stat-name">Vitamins &amp; Minerals</div></div>
    </div>
  </section>

  <section class="label label--strawberry">
    <svg class="swoosh" viewBox="0 0 360 320" aria-hidden="true">
      <rect class="strip" x="0" y="0" width="40" height="320"/>
      <path class="band" d="M40 0 H140 C112 60 100 110 84 180 C70 240 60 290 56 320 H40 Z"/>
      <path class="edge" d="M140 0 C112 60 100 110 84 180 C70 240 60 290 56 320"/>
    </svg>
    <div class="brand"><span class="brand-name">VELTRA</span></div>
    <span class="brand-sub">NUTRITION</span>
    <div class="title">
      <div class="title-diet">DIET</div>
      <div class="title-protein">PROTEIN</div>
      <div class="title-power">POWER</div>
    </div>
    <div class="flavour-art" role="img" aria-label="Photo of fresh strawberries"></div>
    <div class="rule"></div>
    <p class="claims">High Protein<br>Low Carbohydrates</p>
    <div class="flavour-tag">STRAWBERRY</div>
    <p class="net-weight">NET WT. 6lb (2.727G)</p>
    <div class="stats">
      <div><div class="stat-value stat-value--cal">1050</div><div class="stat-name">Calories</div></div>
      <div><div class="stat-value stat-value--protein">60G</div><div class="stat-name">Protein</div></div>
      <div><div class="stat-value stat-value--carbs">250G+</div><div class="stat-name">Carbs</div></div>
      <div><div class="stat-value stat-value--vit">30</div><div class="stat-name">Vitamins &amp; Minerals</div></div>
    </div>
  </section>

  <section class="label label--banana">
    <svg class="swoosh" viewBox="0 0 360 320" aria-hidden="true">
      <rect class="strip" x="0" y="0" width="40" height="320"/>
      <path class="band" d="M40 0 H140 C112 60 100 110 84 180 C70 240 60 290 56 320 H40 Z"/>
      <path class="edge" d="M140 0 C112 60 100 110 84 180 C70 240 60 290 56 320"/>
    </svg>
    <div class="brand"><span class="brand-name">VELTRA</span></div>
    <span class="brand-sub">NUTRITION</span>
    <div class="title">
      <div class="title-diet">DIET</div>
      <div class="title-protein">PROTEIN</div>
      <div class="title-power">POWER</div>
    </div>
    <div class="flavour-art" role="img" aria-label="Photo of a bunch of bananas"></div>
    <div class="rule"></div>
    <p class="claims">High Protein<br>Low Carbohydrates</p>
    <div class="flavour-tag">BANANA</div>
    <p class="net-weight">NET WT. 6lb (2.727G)</p>
    <div class="stats">
      <div><div class="stat-value stat-value--cal">1050</div><div class="stat-name">Calories</div></div>
      <div><div class="stat-value stat-value--protein">60G</div><div class="stat-name">Protein</div></div>
      <div><div class="stat-value stat-value--carbs">250G+</div><div class="stat-name">Carbs</div></div>
      <div><div class="stat-value stat-value--vit">30</div><div class="stat-name">Vitamins &amp; Minerals</div></div>
    </div>
  </section>

</main>
</body>
</html>
```